Brightwell Power Systems

We'd like a web design that's beautiful and professional. We replace existing inefficient systems (mostly lighting at the moment but expanding) with highly efficient systems.

```html
<!DOCTYPE html>
<html lang="en">
<head>
<meta charset="utf-8">
<title>Brightwell Power Systems</title>
<link href="https://fonts.googleapis.com/css2?family=Arimo:wght@400;700&family=Noto+Sans:wght@400;700&family=PT+Sans:wght@400;700&display=swap" rel="stylesheet">
<style>
:root{
  --green:#1a9a3e;
  --green-dark:#0f7a2c;
  --ink:#3a3a3a;
  --muted:#666;
  --page-top:#f4f4f4;
  --band:#d9d9d9;
  --band-dark:#c4c4c4;
  --footer:#262626;
  --footer-deep:#1b1b1b;
  --orange:#d98a1e;
}
*{margin:0;padding:0;box-sizing:border-box}
html,body{width:680px;height:1200px;overflow:hidden}
body{position:relative;font-family:"Noto Sans",sans-serif;color:var(--ink);
  background:linear-gradient(var(--page-top) 0,var(--page-top) 290px,#e2e2e2 290px,#cfcfcf 662px,#e6e6e6 662px,#cdcdcd 978px)}
.abs{position:absolute}
.header{left:26px;top:0;width:625px;height:94px;background:linear-gradient(#fff,#d6d6d6)}
.brand{left:34px;top:30px;display:flex;align-items:center;gap:8px;font-family:"PT Sans",sans-serif;font-weight:700;font-size:17px;color:var(--green);line-height:1.05}
.brand-mark{width:14px;height:14px;background:var(--green);flex:none}
.contact-top{right:40px;top:26px;display:flex;gap:14px;align-items:center;font-size:8px;color:#888}
.contact-top span{display:flex;align-items:center;gap:4px}
.social{display:flex;gap:4px}
.social i{width:16px;height:16px;border-radius:50%;display:block}
.nav{left:236px;top:58px;width:415px;height:30px;background:var(--green);display:flex;font-family:"Arimo",sans-serif;font-size:9px;color:#fff}
.nav a{display:flex;align-items:center;padding:0 10px;border-right:1px solid rgba(255,255,255,.25);color:#fff;text-decoration:none;white-space:nowrap}
.nav a.active{background:#111;padding:0 14px}
.nav-cut{left:236px;top:58px}
.hero{left:26px;top:94px;width:625px;height:228px;background:#0c0c0c;overflow:hidden}
.hero-photo{left:0;top:0;width:420px;height:228px;background:radial-gradient(ellipse at 50% 70%,#8d979c 0,#3d4548 40%,#101314 80%)}
.hero-tag{left:72px;top:60px;font-family:"PT Sans",sans-serif;font-size:14px;color:#fff;white-space:nowrap}
.hero-tag b{color:var(--green);font-weight:400}
.why{left:402px;top:28px;color:#fff;font-family:"PT Sans",sans-serif;white-space:nowrap}
.why h2{font-weight:400;font-size:13px;margin-bottom:10px}
.why li{list-style:none;display:flex;align-items:center;gap:12px;font-size:12px;height:28px}
.btn-learn{left:501px;top:172px;width:87px;height:25px;border-radius:3px;background:var(--green);color:#fff;font-size:8.5px;display:flex;align-items:center;justify-content:center;font-family:"Arimo",sans-serif}
.section-title{left:0;width:680px;text-align:center;font-family:"PT Sans",sans-serif;font-size:14px}
.rule{height:1px;background:#b5b5b5}
.intro{left:116px;top:400px;width:448px;font-size:7.6px;line-height:16.5px;color:#666;text-align:justify}
.product{width:116px;height:116px;border-radius:50%;background:#bdbdbd;border:5px solid #e8e8e8;box-shadow:0 0 0 2px #b0b0b0}
.product div{width:100%;height:100%;border-radius:50%}
.arrow{font-family:"Arimo",sans-serif;font-size:30px;color:#777}
.traits{top:742px;font-size:7.8px;line-height:13px;color:#555}
.traits li{list-style:none;display:flex;gap:8px;margin-bottom:13px}
.traits li.plain{padding-left:18px}
.traits svg{flex:none;margin-top:2px}
.cta{top:938px;height:24px;display:flex;align-items:center;color:#fff;font-family:"PT Sans",sans-serif;font-size:9px;white-space:nowrap;overflow:hidden}
.cta i{display:flex;align-items:center;justify-content:center;width:28px;height:100%;border-right:1px solid rgba(0,0,0,.25);flex:none}
.cta span{padding:0 6px}
.footer{left:0;top:978px;width:680px;height:192px;background:linear-gradient(180deg,#2c2c2c,var(--footer))}
.f-col{top:24px;color:#fff;font-family:"Arimo",sans-serif}
.f-col h3{font-weight:400;font-size:11.5px;padding-bottom:10px;border-bottom:1px solid #444;width:145px;margin-bottom:12px;white-space:nowrap}
.f-col li{list-style:none;font-size:8px;height:20px;display:flex;align-items:center;gap:8px;white-space:nowrap}
.dot{width:4px;height:4px;border-radius:50%;background:#fff}
.copyright{left:0;top:1170px;width:680px;height:30px;background:var(--footer-deep);color:#ccc;font-family:"Arimo",sans-serif;font-size:7px;display:flex;align-items:center;justify-content:center}
</style>
</head>
<body>
<header class="abs header"></header>
<div class="abs brand"><span class="brand-mark"></span><span>BRIGHTWELL<br>POWER SYSTEMS</span></div>
<div class="abs contact-top">
  <span><svg width="9" height="7" viewBox="0 0 9 7"><path d="M0 2Q4.5-1 9 2L8 3.5 6.5 2.5H2.5L1 3.5Z M2 3H7L8 7H1Z" fill="#1a9a3e"/></svg>1-800-555-0142</span>
  <span><svg width="9" height="7" viewBox="0 0 9 7"><rect width="9" height="7" fill="#1a9a3e"/><path d="M0 0L4.5 4 9 0" stroke="#fff" fill="none"/></svg>your@email.com</span>
  <span class="social"><i style="background:#4b7ba6"></i><i style="background:#4aa3df"></i><i style="background:#3b5998"></i><i style="background:#d3302a"></i></span>
</div>
<nav class="abs nav">
  <a class="active">HOME</a><a>WHY LED?</a><a>CASE STUDIES</a><a>FAQ</a><a>ENERGY AUDIT</a><a style="border:0">CONTACT</a>
</nav>
<svg class="abs nav-cut" width="14" height="30"><path d="M0 30L14 0V30Z" fill="#111"/></svg>

<section class="abs hero">
  <div class="abs hero-photo" role="img" aria-label="LED light fixtures glowing in a dark showroom"></div>
  <div class="abs" style="left:380px;top:0;width:120px;height:228px;background:linear-gradient(90deg,rgba(12,12,12,0),#0c0c0c)"></div>
  <p class="abs hero-tag">PROMOTING <b>ENERGY</b> INDEPENDENCE</p>
  <div class="abs why">
    <h2>WHY BRIGHTWELL POWER SYSTEMS?</h2>
    <ul>
      <li><svg width="14" height="11" viewBox="0 0 14 11"><path d="M1 6L5 10 13 1" stroke="#fff" stroke-width="2.6" fill="none"/></svg>Light to no up front cost</li>
      <li><svg width="14" height="11" viewBox="0 0 14 11"><path d="M1 6L5 10 13 1" stroke="#fff" stroke-width="2.6" fill="none"/></svg>Up to 90% more efficient</li>
      <li><svg width="14" height="11" viewBox="0 0 14 11"><path d="M1 6L5 10 13 1" stroke="#fff" stroke-width="2.6" fill="none"/></svg>Lower long-term maintenance</li>
      <li><svg width="14" height="11" viewBox="0 0 14 11"><path d="M1 6L5 10 13 1" stroke="#fff" stroke-width="2.6" fill="none"/></svg>Request a free energy audit</li>
    </ul>
  </div>
  <div class="abs btn-learn">LEARN MORE</div>
</section>

<svg class="abs" style="left:330px;top:334px" width="20" height="20"><circle cx="10" cy="10" r="9" fill="none" stroke="#999" stroke-width="1.2"/><circle cx="10" cy="9" r="3.2" fill="none" stroke="#999"/><path d="M8.5 13H11.5" stroke="#999"/></svg>
<h1 class="abs section-title" style="top:360px;color:var(--green);font-weight:400">Welcome To Brightwell Power Systems</h1>
<div class="abs rule" style="left:113px;top:387px;width:454px"></div>
<p class="abs intro">Brightwell Power Systems is an acknowledged Green Energy leader providing energy saving lighting solutions. Our certified trained professionals coupled with our close relationships with the leading LED manufacturers around the world, ensures that your LED retrofit project will be affordable; saving you up to 75% on your lighting costs and drastically reducing replacement costs. Our turn-key system takes care of everything from the initial lighting energy audit, to an energy saving solution, to professional installation, and finally complete cleanup and proper disposal.</p>

<span class="abs arrow" style="left:92px;top:538px">&#8249;</span>
<div class="abs product" style="left:120px;top:500px"><div role="img" aria-label="Round LED work light" style="background:radial-gradient(#fff 45%,#f2f2f2)"></div></div>
<div class="abs product" style="left:283px;top:500px"><div role="img" aria-label="LED spotlight bulb" style="background:radial-gradient(#fff 45%,#f2f2f2)"></div></div>
<div class="abs product" style="left:445px;top:500px"><div role="img" aria-label="Three recessed LED puck lights" style="background:radial-gradient(#fff 45%,#f2f2f2)"></div></div>
<span class="abs arrow" style="left:574px;top:538px">&#8250;</span>
<div class="abs rule" style="left:144px;top:640px;width:413px;background:#bbb"></div>

<svg class="abs" style="left:329px;top:673px" width="22" height="22"><circle cx="11" cy="11" r="9.5" fill="none" stroke="#777" stroke-width="1.4"/><text x="11" y="15" text-anchor="middle" font-size="11" font-family="Arimo,sans-serif" font-weight="700" fill="#777">?</text></svg>
<h2 class="abs section-title" style="top:694px;color:#444;font-weight:400">Why we are unique?</h2>
<div class="abs rule" style="left:74px;top:722px;width:532px"></div>

<ul class="abs traits" style="left:74px;width:256px">
  <li><svg width="10" height="9" viewBox="0 0 10 9"><path d="M1 5L4 8 9 1" stroke="#1a9a3e" stroke-width="2" fill="none"/></svg><span>Established in 1986 with 25 years of outstanding service, a GSA approved vendor</span></li>
  <li><svg width="10" height="9" viewBox="0 0 10 9"><path d="M1 5L4 8 9 1" stroke="#1a9a3e" stroke-width="2" fill="none"/></svg><span>A Service-Disabled Veteran-Owned company focused on hiring Service Disabled Veterans, Veterans and family members of veterans</span></li>
  <li><svg width="10" height="9" viewBox="0 0 10 9"><path d="M1 5L4 8 9 1" stroke="#1a9a3e" stroke-width="2" fill="none"/></svg><span>As a member of the National Green Building Alliance, we support green design, construction and operations</span></li>
  <li><svg width="10" height="9" viewBox="0 0 10 9"><path d="M1 5L4 8 9 1" stroke="#1a9a3e" stroke-width="2" fill="none"/></svg><span>GreenPro (Green Building Professional Design) trained employees<br>DUNS Number - 284610573</span></li>
</ul>
<ul class="abs traits" style="left:351px;width:256px">
  <li><svg width="10" height="9" viewBox="0 0 10 9"><path d="M1 5L4 8 9 1" stroke="#1a9a3e" stroke-width="2" fill="none"/></svg><span>Active in System for Award Management (SAM) - Registration valid until 07/15/2014</span></li>
  <li><svg width="10" height="9" viewBox="0 0 10 9"><path d="M1 5L4 8 9 1" stroke="#1a9a3e" stroke-width="2" fill="none"/></svg><span>Registered NAICS codes - 238210, 335110, 335122</span></li>
  <li class="plain"><span>LED products available on GSA Schedule - GS-07F-0419R</span></li>
  <li><svg width="10" height="9" viewBox="0 0 10 9"><path d="M1 5L4 8 9 1" stroke="#1a9a3e" stroke-width="2" fill="none"/></svg><span>CAGE Code - 7K3M9</span></li>
</ul>
<div class="abs rule" style="left:74px;top:918px;width:532px"></div>

<div class="abs cta" style="left:220px;width:105px;background:var(--orange)"><i><svg width="14" height="12" viewBox="0 0 14 12"><path d="M0 1H3L5 8H12L13 3H4" stroke="#fff" stroke-width="1.3" fill="none"/><circle cx="6" cy="10.5" r="1.2" fill="#fff"/><circle cx="11" cy="10.5" r="1.2" fill="#fff"/></svg></i><span>OUR PRODUCTS</span></div>
<div class="abs cta" style="left:330px;width:139px;background:var(--green)"><i><svg width="14" height="12" viewBox="0 0 14 12"><rect x="1" y="2" width="9" height="9" fill="none" stroke="#fff" stroke-width="1.2"/><path d="M3 6L6 9 13 1" stroke="#fff" stroke-width="1.8" fill="none"/></svg></i><span>REQUEST A FREE AUDIT</span></div>

<footer class="abs footer">
  <div class="abs f-col" style="left:70px">
    <h3>QUICKLINKS</h3>
    <div style="display:flex;gap:30px">
      <ul><li><i class="dot"></i>Home</li><li><i class="dot"></i>Why LED?</li><li><i class="dot"></i>Case Studies</li></ul>
      <ul><li><i class="dot"></i>FAQ</li><li><i class="dot"></i>Energy Audit</li><li><i class="dot"></i>Contact</li></ul>
    </div>
    <div style="display:flex;gap:5px;margin-top:10px"><i style="width:14px;height:14px;border-radius:50%;background:#777"></i><i style="width:14px;height:14px;border-radius:50%;background:#777"></i><i style="width:14px;height:14px;border-radius:50%;background:#777"></i><i style="width:14px;height:14px;border-radius:50%;background:#777"></i></div>
  </div>
  <div class="abs f-col" style="left:253px">
    <h3>CONTACT INFORMATION</h3>
    <ul>
      <li><svg width="9" height="8" viewBox="0 0 9 8"><path d="M0 4L4.5 0 9 4H7.5V8H1.5V4Z" fill="#fff"/></svg>Loc: 123 Address, City. Country</li>
      <li><svg width="9" height="7" viewBox="0 0 9 7"><path d="M0 2Q4.5-1 9 2L8 3.5 6.5 2.5H2.5L1 3.5Z M2 3H7L8 7H1Z" fill="#fff"/></svg>Tel: 02-1234-567890</li>
      <li><svg width="9" height="7" viewBox="0 0 9 7"><rect width="9" height="7" fill="#fff"/><path d="M0 0L4.5 4 9 0" stroke="#262626" fill="none"/></svg>Email: your@email.com</li>
      <li><svg width="9" height="7" viewBox="0 0 9 7"><rect width="9" height="7" fill="#fff"/><path d="M0 0L4.5 4 9 0" stroke="#262626" fill="none"/></svg>Chat: your@email.com</li>
    </ul>
  </div>
  <div class="abs f-col" style="left:456px">
    <h3>THE BOTTOMLINE</h3>
    <ul><li><i class="dot"></i>The Savings</li><li><i class="dot"></i>LED Retrofit Process</li><li><i class="dot"></i>Tax Incentives</li><li><i class="dot"></i>Utility Rebates</li></ul>
  </div>
</footer>
<div class="abs copyright">Copyright © 2013. Brightwell Power Systems All Rights Reserved.</div>
</body>
</html>
```